Welding and farication business card

Business name Tbm Welding & Fabrication

I need a business card made for my welding and fabrication business that is bold and stands out. My business is both welding repairs on machinery and anything else you can imagine as well as fabricating new products. i have used this service before and was very happy with the out come of my design logo. i think the card should remain fairly simple and classy but also be bold. I think a black card would best be suited to the talk with my logo on it. i feel the back of the card should just have my logo and the front have my logo email, website and phone number and maybe incorporate a facebook and instagram simple if it can be made look good these arnt a necessity.
I have included both my logo and some business card ideas below

Target Market(s)

Farmers, heavy industry, earthmoving, trucking

Industry/Entity Type

Engineering

Contact Information for Business Card

0438517264
dale@tbmweldingandfabrication.com.au
www.tbmweldingandfabrication.com.au

Colors
33a6d7
0255a3

Requirements
Must have
• Dale Hutchins
my phone number 0438517264
my logo
Preferably a black card desgn
Nice to have
• List of what i do,
Sheds and carports
Ute trays
Stockyards
Trailers
Farm equipment
Stockcrates
Gateways and Entrances
Breakdowns
Maintenance
And lots more!

```html
<!DOCTYPE html>
<html lang="en">
<head>
<meta charset="utf-8">
<title>Tbm Welding &amp; Fabrication – Business Card</title>
<link rel="stylesheet" href="https://fonts.googleapis.com/css2?family=Josefin+Sans:wght@300;400;600&display=swap">
<style>
  :root {
    --page-bg: #2a2a2c;
    --card-dark: #1d1d1f;
    --card-dark-2: #262628;
    --card-white: #f4f4f5;
    --edge-grey: #d3d4d6;
    --brand-blue: #0255a3;
    --brand-sky: #33a6d7;
    --band-blue: #1f64a8;
    --text-light: #d9dadc;
  }
  * { box-sizing: border-box; margin: 0; padding: 0; }
  html, body {
    width: 1200px; height: 900px; overflow: hidden;
    background: var(--page-bg);
    font-family: "Josefin Sans", sans-serif;
  }
  .business-card {
    position: absolute; left: 120px; top: 160px;
    width: 960px; height: 580px;
    border-radius: 40px;
    box-shadow: 0 24px 60px rgba(0,0,0,.55);
  }
  .card-shapes { position: absolute; inset: 0; }
  .service-list {
    position: absolute; left: 56px; top: 34px;
    list-style: none;
    color: var(--text-light);
    font-weight: 300; font-size: 20px; line-height: 25px;
  }
  .service-list li::before { content: "• "; }
  .contact-list {
    position: absolute; left: 40px; top: 292px;
    list-style: none;
    color: #e8eef6;
    font-weight: 300; font-size: 19px;
  }
  .contact-list li { display: flex; align-items: center; gap: 12px; height: 40px; }
  .contact-icon { width: 26px; height: 26px; flex: none; }
  .brand-lockup {
    position: absolute; left: 545px; top: 110px;
    display: flex; align-items: center; gap: 16px;
    color: var(--brand-blue);
    font-weight: 600; font-size: 34px; line-height: 1.15;
  }
  .brand-dot {
    width: 22px; height: 22px; border-radius: 50%;
    background: var(--brand-blue); flex: none;
  }
  .holder-name {
    position: absolute; left: 560px; top: 392px;
    color: var(--brand-sky);
    font-weight: 400; font-size: 40px; letter-spacing: 2px;
    text-transform: uppercase;
  }
</style>
</head>
<body>
<article class="business-card">
  <svg class="card-shapes" viewBox="0 0 960 580" width="960" height="580" aria-hidden="true">
    <defs>
      <clipPath id="card-edge"><rect width="960" height="580" rx="40"/></clipPath>
    </defs>
    <g clip-path="url(#card-edge)">
      <rect class="card-face" width="960" height="580" fill="var(--card-white)"/>
      <polygon class="edge-stripe" points="0,0 528,0 478,340 438,440 358,580 0,580" fill="var(--edge-grey)"/>
      <polygon class="dark-panel" points="0,0 510,0 460,340 420,440 340,580 0,580" fill="var(--card-dark)"/>
      <polygon class="contact-band" points="0,270 475,270 452,370 420,440 0,440" fill="var(--band-blue)"/>
      <polygon class="name-band" points="500,330 960,330 960,500 432,500 462,440 482,380" fill="var(--card-dark-2)"/>
    </g>
  </svg>

  <ul class="service-list">
    <li>Sheds and carports</li>
    <li>Ute trays</li>
    <li>Stockyards</li>
    <li>Trailers</li>
    <li>Farm equipment</li>
    <li>Stockcrates</li>
    <li>Gateways and Entrances</li>
    <li>Breakdowns</li>
    <li>Maintenance, And lots more!</li>
  </ul>

  <ul class="contact-list">
    <li>
      <svg class="contact-icon" viewBox="0 0 26 26" aria-hidden="true"><circle cx="13" cy="13" r="12" fill="#e8eef6"/><path d="M9 7l3 3-2 2c1 2 2 3 4 4l2-2 3 3-2 2c-5-1-9-5-10-10z" fill="var(--band-blue)"/></svg>
      <span>0438517264</span>
    </li>
    <li>
      <svg class="contact-icon" viewBox="0 0 26 26" aria-hidden="true"><circle cx="13" cy="13" r="12" fill="#e8eef6"/><rect x="7" y="9" width="12" height="9" fill="none" stroke="var(--band-blue)" stroke-width="1.6"/><path d="M7 9l6 5 6-5" fill="none" stroke="var(--band-blue)" stroke-width="1.6"/></svg>
      <span>dale@tbmweldingandfabrication.com.au</span>
    </li>
    <li>
      <svg class="contact-icon" viewBox="0 0 26 26" aria-hidden="true"><circle cx="13" cy="13" r="12" fill="#e8eef6"/><circle cx="13" cy="13" r="6.5" fill="none" stroke="var(--band-blue)" stroke-width="1.5"/><path d="M6.5 13h13M13 6.5c-3 3.5-3 9.5 0 13M13 6.5c3 3.5 3 9.5 0 13" fill="none" stroke="var(--band-blue)" stroke-width="1.3"/></svg>
      <span>www.tbmweldingandfabrication.com.au</span>
    </li>
  </ul>

  <div class="brand-lockup">
    <span class="brand-dot"></span>
    <span class="brand-name">Tbm Welding<br>&amp; Fabrication</span>
  </div>

  <p class="holder-name">Dale Hutchins</p>
</article>
</body>
</html>
```